Chiropractic Software Company needs Business Cards

We need a bushiness card design for use at a Chiropractic conference. We build billing, practice management, and medical documentation software. Our product is Vantora Chiropractic Software(Vantora for short). On top of our software we have practice success coaches that coordinate with our chiropractor clients to help them grow their practice and treat more patients. Our logo colors are tried-and-true orange-and-blue. We'd like a sterile white background and a clean layout; organizing the following information: Name, Position/Title, Phone Number, Address, email, and our website. On the backside we'd like our Logo and our slogan, "Your Clinic Keel" and our website(http://www.vantorachiropracticsoftware.example)

Industry/Entity Type

Business

```html
<!DOCTYPE html>
<html lang="en">
<head>
<meta charset="utf-8">
<title>Vantora Chiropractic Software – Business Card</title>
<link rel="stylesheet" href="https://fonts.googleapis.com/css2?family=Lato:wght@400;700;900&display=swap">
<style>
  :root {
    --backdrop: #e4e5e8;
    --paper: #ffffff;
    --blue: #1f5fb4;
    --blue-deep: #1d3f9a;
    --orange: #f28a2e;
    --orange-light: #f9a84e;
    --ink: #1b1b1b;
    --rule: #9a9a9a;
  }
  * { box-sizing: border-box; margin: 0; padding: 0; }
  html, body {
    width: 1200px; height: 926px; overflow: hidden;
    background: var(--backdrop);
    font-family: "Lato", sans-serif;
  }
  .sheet {
    width: 1200px; height: 926px;
    display: flex; flex-direction: column; align-items: center; justify-content: center;
    gap: 60px;
  }
  .card {
    position: relative;
    width: 680px; height: 389px;
    background: var(--paper);
    box-shadow: 0 6px 18px rgba(0,0,0,0.18);
    overflow: hidden;
  }
  .brand {
    display: flex; align-items: center; gap: 10px;
    color: var(--blue);
    font-weight: 900;
    letter-spacing: 1px;
  }
  .brand-dot { border-radius: 50%; background: var(--orange); flex: none; }

  /* Back side */
  .card-back { display: flex; flex-direction: column; align-items: center; justify-content: center; }
  .card-back .brand { font-size: 40px; }
  .card-back .brand-dot { width: 44px; height: 44px; }
  .slogan {
    margin-top: 22px;
    color: var(--blue);
    font-weight: 700;
    font-size: 38px;
  }
  .back-web {
    margin-top: 14px;
    color: var(--ink);
    font-size: 14px;
    letter-spacing: 3.2px;
  }

  /* Front side */
  .card-front .brand {
    position: absolute; left: 190px; top: 62px;
    font-size: 32px;
  }
  .card-front .brand-dot { width: 36px; height: 36px; }
  .identity {
    position: absolute; right: 350px; top: 160px;
    text-align: right;
  }
  .person-name { color: var(--blue-deep); font-size: 31px; font-weight: 400; line-height: 1; }
  .person-name strong { font-weight: 900; }
  .person-title { margin-top: 4px; font-size: 13px; font-weight: 900; color: var(--ink); letter-spacing: 0.5px; }
  .divider {
    position: absolute; left: 342px; top: 158px;
    width: 1px; height: 92px; background: var(--rule);
  }
  .contact {
    position: absolute; left: 352px; top: 158px;
    list-style: none;
    font-size: 14.5px; color: var(--ink); line-height: 19px;
  }
  .contact li { display: flex; }
  .contact .key { width: 16px; color: var(--orange); font-weight: 900; font-size: 12px; }
  .contact .cont { padding-left: 16px; }
  .swoosh { position: absolute; left: 0; top: 0; }
</style>
</head>
<body>
<main class="sheet">

  <section class="card card-back" aria-label="Card back">
    <div class="brand"><span class="brand-dot"></span>Vantora</div>
    <p class="slogan">Your Clinic Keel</p>
    <p class="back-web">www.vantorachiropracticsoftware.example</p>
  </section>

  <section class="card card-front" aria-label="Card front">
    <svg class="swoosh" width="680" height="389" viewBox="0 0 680 389" aria-hidden="true">
      <defs>
        <linearGradient id="orangeFill" x1="0" y1="0" x2="0" y2="1">
          <stop offset="0" stop-color="var(--orange-light)"/>
          <stop offset="1" stop-color="var(--orange)"/>
        </linearGradient>
        <linearGradient id="blueFill" x1="0" y1="0" x2="1" y2="0">
          <stop offset="0" stop-color="#2a72cf"/>
          <stop offset="1" stop-color="var(--blue-deep)"/>
        </linearGradient>
      </defs>
      <path d="M0,282 C160,330 320,344 680,332 L680,389 L0,389 Z" fill="url(#orangeFill)"/>
      <path d="M0,222 C120,258 270,318 680,326 L680,331 C320,340 160,322 0,276 Z" fill="url(#blueFill)"/>
      <path d="M0,279 C160,326 320,340 680,330" fill="none" stroke="#ffffff" stroke-width="3"/>
    </svg>

    <div class="brand"><span class="brand-dot"></span>Vantora</div>

    <div class="identity">
      <p class="person-name">John <strong>Smith</strong></p>
      <p class="person-title">TTLE HERE</p>
    </div>
    <span class="divider"></span>
    <ul class="contact">
      <li><span class="key">P</span>: +123 456 7890</li>
      <li><span class="key">W</span>: vantorachiropracticsoftware.example</li>
      <li><span class="key">E</span>: yourname@yourdomailn.com</li>
      <li><span class="key">A</span>: Street address goes here,</li>
      <li><span class="key"></span>Suite #303, Alt Bldg, NY 82365</li>
    </ul>
  </section>

</main>
</body>
</html>
```